Online Nutrition Consulting Website/healthy lifestyle

This is a website for online nutrition consulting. (For example, weight loss.) The company is called Mirela's. I included the logo so you have a feel for the colors and the message of the company. I would like to have one main neutral color in there. (I am leaning toward grey, but I am open to ideas) I would like the design to be simple and to the point.

My ultimate goal is for my website to stand out from other nutrition websites by projecting my slogan (It's not a diet. It's a lifestyle.)

Target Market(s)

Health-conscious people.

Industry/Entity Type

Nutrition

Coding

Coded - Design and coding required

Number of Pages Required

4 page

Font styles to use
Script

Requirements
Must have
• Home page, Services page , About page, and a Blog page. (Once I see the layout, I will give you more detail so it isn't confusing. For example: payment of services and the "About me")
• Logo must be included.
• Easy navigation. Not too much scrolling.

```html
<!DOCTYPE html>
<html lang="en">
<head>
<meta charset="utf-8">
<title>Mirela's — Latest Blog</title>
<link href="https://fonts.googleapis.com/css2?family=Great+Vibes&family=Open+Sans:wght@400;600;700&display=swap" rel="stylesheet">
<style>
:root{
  --green:#8cc63f;
  --green-dark:#6fa82a;
  --navy:#1f2a3a;
  --footer:#2b2f36;
  --grey-bg:#f4f5f6;
  --line:#e2e4e6;
  --text:#555a60;
  --muted:#9aa0a6;
  --head:#2e3338;
  --blue:#35a6e0;
  --white:#ffffff;
}
*{box-sizing:border-box;margin:0;padding:0}
html,body{width:1200px;height:2316px;overflow:hidden}
body{position:relative;background:var(--white);font-family:'Open Sans',Arial,sans-serif;color:var(--text);font-size:12px}
.abs{position:absolute}

/* header */
.site-header{left:0;top:0;width:1200px;height:128px;background:var(--white)}
.brand{left:112px;top:34px;display:flex;align-items:center;gap:12px}
.brand-dot{width:40px;height:40px;border-radius:50%;background:var(--green)}
.brand-name{font-family:'Open Sans',Arial,sans-serif;font-weight:700;font-size:34px;color:var(--green-dark);line-height:1}
.brand-tag{left:164px;top:84px;font-size:10px;color:var(--muted);letter-spacing:.5px}
.social{right:164px;top:12px;display:flex;gap:10px}
.social span{width:30px;height:30px;border-radius:4px;background:var(--navy)}
.contact{right:112px;top:62px;display:flex;gap:28px;font-size:11px;color:var(--head)}
.contact span{display:flex;align-items:center;gap:6px}

/* nav */
.main-nav{left:0;top:128px;width:1200px;height:40px;background:var(--green)}
.main-nav ul{position:absolute;left:112px;top:0;list-style:none;display:flex;height:40px}
.main-nav li{color:var(--white);font-size:13px;font-weight:600;line-height:40px;padding:0 16px}
.main-nav li.active{background:var(--green-dark)}
.nav-search{right:112px;top:11px}

/* banner */
.banner{left:0;top:168px;width:1200px;height:170px;background:var(--grey-bg);border-bottom:1px solid var(--line)}
.banner h1{position:absolute;left:112px;top:48px;font-family:'Great Vibes',cursive;font-weight:400;font-size:60px;color:var(--green-dark)}
.banner-photo{position:absolute;left:760px;top:0;width:340px;height:170px;background:linear-gradient(90deg,var(--grey-bg),#e9e2d6 40%,#d8c9b6)}

/* posts */
.post{left:112px;width:680px}
.post-media{width:680px;position:relative}
.media-gallery{height:330px;background:linear-gradient(120deg,#3a3f47,#7b6a5e 55%,#c9a58b)}
.media-standard{height:350px;background:linear-gradient(120deg,#f2f2f0,#e7dccd 50%,#cfe0b8)}
.media-video{height:370px;background:linear-gradient(160deg,#8ea7c0,#b7c0c6 50%,#6d6a66)}
.dots{position:absolute;left:50%;bottom:14px;transform:translateX(-50%);display:flex;gap:6px}
.dots i{width:8px;height:8px;border-radius:50%;background:rgba(255,255,255,.6)}
.dots i.on{background:var(--white)}
.video-bar{position:absolute;left:0;bottom:0;width:680px;height:30px;background:rgba(20,24,30,.75)}
.video-bar .prog{position:absolute;left:14px;top:13px;width:560px;height:4px;background:rgba(255,255,255,.3)}
.video-bar .prog b{display:block;width:120px;height:4px;background:var(--green)}
.video-tools{position:absolute;right:12px;top:12px;display:flex;flex-direction:column;gap:6px}
.video-tools span{width:26px;height:26px;background:rgba(20,24,30,.7)}
.post-body{position:relative;margin-top:24px;padding-left:66px;padding-right:50px}
.author{position:absolute;left:0;top:0;width:52px;text-align:center;font-size:10px;color:var(--muted)}
.author .av{width:44px;height:44px;border-radius:50%;background:#c9b7a5;margin:0 auto 6px;border:2px solid var(--line)}
.author .kind{width:30px;height:30px;border-radius:50%;background:var(--head);margin:8px auto 0}
.post-body h2{font-size:18px;font-weight:600;color:var(--head);margin-bottom:6px}
.meta{font-size:10px;color:var(--muted);margin-bottom:10px}
.meta b{color:var(--blue);font-weight:400}
.post-body p{font-size:11px;line-height:18px;color:var(--text)}
.more{display:inline-block;margin-top:10px;font-size:11px;color:var(--blue)}
.share{position:absolute;right:0;top:0;width:32px;height:32px;border-radius:50%;background:var(--blue)}
.post-sep{left:112px;width:680px;height:1px;background:var(--line)}

/* pagination */
.pager{left:112px;top:2186px;display:flex;gap:4px}
.pager span{height:28px;min-width:28px;padding:0 10px;line-height:28px;font-size:11px;text-align:center;background:#dfe2e5;color:var(--text)}
.pager span.on{background:var(--green);color:var(--white)}

/* sidebar */
.sidebar{left:840px;top:360px;width:260px}
.widget{margin-bottom:28px}
.widget h3{font-size:14px;font-weight:600;color:var(--head);margin-bottom:14px}
.field{height:30px;border:1px solid var(--line);margin-bottom:8px;font-size:10px;color:var(--muted);line-height:28px;padding:0 10px}
.btn{height:32px;background:var(--green);color:var(--white);font-size:12px;font-weight:600;text-align:center;line-height:32px}
.widget p{font-size:11px;line-height:18px}
.tabs{display:flex;margin-bottom:12px}
.tabs span{flex:1;height:28px;line-height:28px;text-align:center;font-size:10px;font-weight:600;background:#eceef0;color:var(--text)}
.tabs span.on{background:var(--green);color:var(--white)}
.combo-item{padding:8px 0;border-bottom:1px solid var(--line);font-size:11px}
.combo-item small{display:block;font-size:9px;color:var(--muted)}
.tweet{display:flex;gap:10px;margin-bottom:12px;font-size:10px;line-height:15px}
.tweet i{flex:none;width:20px;height:20px;background:var(--navy);border-radius:3px}
.tweet small{display:block;color:var(--blue)}
.archives li{list-style:none;display:flex;align-items:center;gap:10px;font-size:11px;padding:6px 0;border-bottom:1px solid var(--line)}
.archives li i{width:12px;height:12px;background:var(--navy)}
.archives li.on{color:var(--green-dark)}
.archives li.on i{background:var(--green)}

/* footer */
.site-footer{left:0;top:2256px;width:1200px;height:60px;background:var(--footer)}
.site-footer ul{position:absolute;left:112px;top:0;list-style:none;display:flex;gap:28px;line-height:60px;color:#d5d8dc;font-size:12px}
.site-footer .copy{position:absolute;right:112px;top:0;line-height:60px;font-size:10px;color:#9aa0a6}
</style>
</head>
<body>

<header class="site-header abs">
  <div class="brand abs"><span class="brand-dot"></span><span class="brand-name">Mirela's</span></div>
  <div class="brand-tag abs">It's not a diet. It's a lifestyle.</div>
  <div class="social abs"><span></span><span></span><span></span></div>
  <div class="contact abs">
    <span><svg width="12" height="10" viewBox="0 0 12 10"><rect x=".5" y=".5" width="11" height="9" fill="none" stroke="#1f2a3a"/><path d="M.5 .5 6 5 11.5 .5" fill="none" stroke="#1f2a3a"/></svg>hello@mirelas-nutrition.com</span>
    <span><svg width="10" height="12" viewBox="0 0 10 12"><rect x="1" y=".5" width="8" height="11" rx="1.5" fill="none" stroke="#1f2a3a"/><circle cx="5" cy="9.5" r=".8" fill="#1f2a3a"/></svg>+1 555 014 2288</span>
  </div>
</header>

<nav class="main-nav abs">
  <ul><li class="active">Home</li><li>About us</li><li>Services</li><li>Payment</li><li>Blog</li><li>Contact us</li></ul>
  <svg class="nav-search abs" width="18" height="18" viewBox="0 0 18 18"><circle cx="7.5" cy="7.5" r="5.5" fill="none" stroke="#fff" stroke-width="2"/><path d="M11.5 11.5 16 16" stroke="#fff" stroke-width="2"/></svg>
</nav>

<section class="banner abs">
  <h1>Latest Blog</h1>
  <div class="banner-photo" role="img" aria-label="Woman resting her head on her arms beside fresh fruit and small dumbbells"></div>
</section>

<article class="post abs" style="top:360px">
  <div class="post-media media-gallery" role="img" aria-label="Smiling woman holding a red apple">
    <div class="dots"><i class="on"></i><i></i><i></i></div>
  </div>
  <div class="post-body">
    <div class="author"><div class="av"></div>By Ana<div class="kind"></div></div>
    <h2>A brand new Set - Gallery Post</h2>
    <div class="meta">Posted in <b>Nutrition, Healthy Life</b> &nbsp;·&nbsp; 12th May 2024</div>
    <p>Simple daily habits make lasting change. Start each morning with water, add colourful vegetables to every plate and keep fresh fruit close at hand for snacks. Small, steady steps build a lifestyle you can enjoy for years.</p>
    <span class="more">Read more →</span>
    <span class="share"></span>
  </div>
</article>
<div class="post-sep abs" style="top:910px"></div>

<article class="post abs" style="top:952px">
  <div class="post-media media-standard" role="img" aria-label="Smiling woman in a green top eating a bowl of salad in a bright kitchen"></div>
  <div class="post-body">
    <div class="author"><div class="av"></div>By Ana<div class="kind"></div></div>
    <h2>A brand new Set for Nutritionist - Standard Post</h2>
    <div class="meta">Posted in <b>Nutrition, Recipes</b> &nbsp;·&nbsp; 28th April 2024</div>
    <p>A balanced plate does not need to be complicated. Fill half with greens, a quarter with lean protein and a quarter with whole grains. Cook at home when you can and enjoy meals slowly with family.</p>
    <span class="more">Read more →</span>
    <span class="share"></span>
  </div>
</article>
<div class="post-sep abs" style="top:1520px"></div>

<article class="post abs" style="top:1552px">
  <div class="post-media media-video" role="img" aria-label="Runner's legs in pink sneakers on an open road">
    <div class="video-tools"><span></span><span></span></div>
    <div class="video-bar"><div class="prog"><b></b></div></div>
  </div>
  <div class="post-body">
    <div class="author"><div class="av"></div>By Ana<div class="kind"></div></div>
    <h2>A brand new Set for Nutritionist - Video Post</h2>
    <div class="meta">Posted in <b>Fitness, Healthy Life</b> &nbsp;·&nbsp; 9th April 2024</div>
    <p>Movement and food work together. A short walk after dinner, a weekend run or a few minutes of stretching all help your body use what you eat. Find an activity you love and keep at it.</p>
    <span class="more">Read more →</span>
    <span class="share"></span>
  </div>
</article>

<div class="pager abs"><span>Prev</span><span class="on">1</span><span>2</span><span>3</span><span>4</span><span>Next</span></div>

<aside class="sidebar abs">
  <div class="widget">
    <h3>Upload Your Article / Videos</h3>
    <div class="field">Name</div>
    <div class="field">Email</div>
    <div class="field">Select a file</div>
    <div class="btn">UPLOAD</div>
  </div>
  <div class="widget">
    <h3>Text Widget</h3>
    <p>Share your favourite recipes and stories with our community. Every article is read by our team before it appears on the blog, so take your time and write from the heart.</p>
  </div>
  <div class="widget">
    <h3>Combo Box</h3>
    <div class="tabs"><span class="on">POPULAR</span><span>RECENT</span><span>COMMENTS</span></div>
    <div class="combo-item">Green smoothie for busy mornings<small>12th May 2024</small></div>
    <div class="combo-item">Five snacks under 150 calories<small>3rd May 2024</small></div>
    <div class="combo-item">How to read a food label<small>28th April 2024</small></div>
    <div class="combo-item">Water, sleep and weight loss<small>20th April 2024</small></div>
  </div>
  <div class="widget">
    <h3>Latest Tweets</h3>
    <div class="tweet"><i></i><div>New meal plan for spring is ready, fresh and simple.<small>2 hours ago</small></div></div>
    <div class="tweet"><i></i><div>Tip of the day: add one more vegetable to lunch.<small>1 day ago</small></div></div>
    <div class="tweet"><i></i><div>Thank you for joining our online consult this week.<small>3 days ago</small></div></div>
  </div>
  <div class="widget">
    <h3>Archives</h3>
    <ul class="archives">
      <li><i></i>January 2024 (3)</li>
      <li><i></i>December 2023 (4)</li>
      <li class="on"><i></i>November 2023 (6)</li>
      <li><i></i>October 2023 (2)</li>
      <li><i></i>September 2023 (5)</li>
      <li><i></i>August 2023 (3)</li>
    </ul>
  </div>
</aside>

<footer class="site-footer abs">
  <ul><li>Home</li><li>About us</li><li>Services</li><li>Payment</li><li>Blog</li><li>Contact us</li></ul>
  <div class="copy">© 2024 www.mirelas-nutrition.com · Privacy Policy</div>
</footer>

</body>
</html>
```